Design and Renovation Company Luxury Business Card

I want to create a luxury business card for a Design and Renovation Firm . We will use our current logo. The company name is 742BUILD. We do not want anything standard. We need a very unique concept.
Please see uploaded inspiration. I really like the textured paper option. I would like the card to be thick with debossing, and/or embossing options. The logo has orange in it but I would like to see the card with and without the orange. I think the orange may make the company feel less high-end. The goal is to elevate the logo not match its vibe per se of the logo. We want something very unique, not standard at all!
I would like a space for :
Logo,
Name,
Position,
Email,
Office number,
Website Address,
Business Address,
Thank you!
Have fun!
Target Market(s)
Home owners Age 35 +
Industry/Entity Type
Design and Renovation
Contact Information for Business Card
Logo, Name, Position, Email, Office number, Website Address, Business Address,.
Colors
Designer to choose colors to be used in the design.
Requirements
Must have
- A luxury designer feel. Must be black or dark grey but open to other luxury ideas.
Nice to have
- Gold, silver, black embossing or debossing. Textured paper design.
Should not have
- A cheap look and feel.

```html
<!DOCTYPE html>
<html lang="en">
<head>
<meta charset="utf-8">
<title>742BUILD Business Card</title>
<link rel="stylesheet" href="https://fonts.googleapis.com/css2?family=Ubuntu:wght@400;500&display=swap">
<style>
  :root {
    --backdrop: #b3b3b3;
    --paper: #ffffff;
    --ink: #0a0a0a;
    --accent: #f7941d;
    --text: #1a1a1a;
  }
  * { margin: 0; padding: 0; box-sizing: border-box; }
  html, body { width: 1200px; height: 1200px; overflow: hidden; }
  body {
    background: var(--backdrop);
    position: relative;
    font-family: "Ubuntu", sans-serif;
    color: var(--text);
  }
  .card {
    position: absolute;
    left: 176px;
    width: 843px;
    height: 494px;
    background: var(--paper);
    overflow: hidden;
    box-shadow: 4px 6px 10px rgba(0,0,0,0.28);
  }
  .card--front { top: 81px; }
  .card--back { top: 625px; }
  .block { position: absolute; }
  .block--ink { background: var(--ink); }
  .block--accent { background: var(--accent); }

  .person { position: absolute; left: 65px; top: 104px; }
  .person__name {
    font-weight: 500;
    font-size: 40px;
    color: var(--accent);
    line-height: 1;
  }
  .person__role { font-size: 23px; margin-top: 8px; }

  .contact-list { position: absolute; left: 65px; top: 208px; list-style: none; }
  .contact-list li {
    display: flex;
    align-items: flex-start;
    font-size: 22px;
    line-height: 28px;
    margin-bottom: 8px;
  }
  .contact-list svg { width: 16px; height: 16px; margin: 6px 14px 0 0; flex: none; fill: var(--accent); }

  .brand-name {
    font-family: "Ubuntu", sans-serif;
    font-weight: 500;
    color: var(--ink);
    line-height: 1;
    white-space: nowrap;
  }
  .front-brand { position: absolute; right: 96px; top: 218px; text-align: right; }
  .front-brand .brand-name { font-size: 54px; }

  .back-brand {
    position: absolute;
    left: 0; right: 0; top: 200px;
    text-align: center;
  }
  .back-brand .brand-name { font-size: 92px; }
  .tagline {
    font-weight: 500;
    font-size: 22px;
    letter-spacing: 2px;
    margin-top: 10px;
    color: var(--ink);
  }
</style>
</head>
<body>

<section class="card card--front">
  <div class="block block--accent" style="left:347px; top:0; width:108px; height:54px;"></div>
  <div class="block block--ink" style="left:244px; top:0; width:151px; height:34px;"></div>

  <div class="block block--accent" style="left:72px; top:411px; width:69px; height:69px;"></div>
  <div class="block block--ink" style="left:0; top:424px; width:108px; height:70px;"></div>

  <div class="person">
    <h1 class="person__name">YOUR NAME</h1>
    <p class="person__role">Designation</p>
  </div>

  <ul class="contact-list">
    <li>
      <svg viewBox="0 0 24 24"><path d="M6.6 10.8a15 15 0 0 0 6.6 6.6l2.2-2.2c.3-.3.7-.4 1-.2 1.1.4 2.3.6 3.6.6.6 0 1 .4 1 1V20c0 .6-.4 1-1 1A17 17 0 0 1 3 4c0-.6.4-1 1-1h3.5c.6 0 1 .4 1 1 0 1.3.2 2.5.6 3.6.1.3 0 .7-.2 1z"/></svg>
      <span>1234 567 890</span>
    </li>
    <li>
      <svg viewBox="0 0 24 24"><path d="M2 5h20v14H2z M4 7v1.2l8 5 8-5V7l-8 5z" fill-rule="evenodd"/></svg>
      <span>mailid@webmail.com</span>
    </li>
    <li>
      <svg viewBox="0 0 24 24"><path d="M12 2a10 10 0 1 0 0 20 10 10 0 0 0 0-20zm0 2c.9 1.2 1.6 2.6 2 4h-4c.4-1.4 1.1-2.8 2-4zM4.3 14a8 8 0 0 1 0-4h3.4a16 16 0 0 0 0 4zm.8 2h3c.3 1.3.8 2.5 1.4 3.6A8 8 0 0 1 5.1 16zm3-8h-3a8 8 0 0 1 4.4-3.6C8.9 5.5 8.4 6.7 8.1 8zM12 20c-.9-1.2-1.600-2.6-2-4h4c-.4 1.4-1.1 2.8-2 4zm2.3-6H9.7a14 14 0 0 1 0-4h4.6a14 14 0 0 1 0 4zm.2 5.6c.6-1.1 1.1-2.300 1.4-3.6h3a8 8 0 0 1-4.4 3.6zm1.8-5.6a16 16 0 0 0 0-4h3.4a8 8 0 0 1 0 4z"/></svg>
      <span>www.website.com</span>
    </li>
    <li>
      <svg viewBox="0 0 24 24"><path d="M12 2a7 7 0 0 0-7 7c0 5.2 7 13 7 13s7-7.8 7-13a7 7 0 0 0-7-7zm0 9.5a2.5 2.5 0 1 1 0-5 2.5 2.5 0 0 1 0 5z"/></svg>
      <span>121/A, Address, Street<br>Pincode - 123456</span>
    </li>
  </ul>

  <div class="front-brand">
    <p class="brand-name">742BUILD</p>
  </div>
</section>

<section class="card card--back">
  <div class="block block--accent" style="left:570px; top:0; width:106px; height:99px;"></div>
  <div class="block block--ink" style="left:465px; top:0; width:152px; height:79px;"></div>

  <div class="block block--accent" style="left:238px; top:459px; width:60px; height:35px;"></div>
  <div class="block block--ink" style="left:86px; top:394px; width:152px; height:100px;"></div>

  <div class="back-brand">
    <p class="brand-name">742BUILD</p>
    <p class="tagline">Design and Renovation Firm</p>
  </div>
</section>

</body>
</html>
```